Business card for Luxury Portable Restroom Trailer company

We are a Luxury Portable Restroom Trailer Company Called PELIKAR HIRES. Based in Orange County California. We provide portable restroom trailers for events, such as, Weddings, Concerts, Charity events, Sporting events, Tournaments, Corporate events, ect. We rent and Sell the Luxury restrooms. Our colors are white, grey, and Orange. As you will see in the logo we uploaded.
There are 2 people in the company so the names and titles will change for the 3 people but card will remain the same. Here is the information for each Person: Dennis Moyle CFO 555 018-3647
next Person: Wesley Tanford VP 555 018-3647
Next Person: Miles Tanford CEO 555 018-3647
Information to include on the card: Luxury Restroom Trailers Rental and Sales. Weddings, Concerts, Charity, Sporting and Corp. Events.

```html
<!DOCTYPE html>
<html lang="en">
<head>
<meta charset="utf-8">
<title>PELIKAR HIRES – Business Card</title>
<link href="https://fonts.googleapis.com/css2?family=Open+Sans:wght@400;600;700;800&display=swap" rel="stylesheet">
<style>
  :root {
    --stage: #232323;
    --orange: #f26a21;
    --grey: #4a4a4a;
    --ink: #222222;
    --paper: #ffffff;
    --peach: #fdf0e6;
    --peach-deep: #fbe3d1;
  }
  * { box-sizing: border-box; margin: 0; padding: 0; }
  html, body { width: 1200px; height: 768px; overflow: hidden; background: var(--stage); }
  body { font-family: "Open Sans", Arial, sans-serif; position: relative; }

  .card {
    position: absolute;
    top: 230px;
    width: 530px;
    height: 303px;
    border-radius: 18px;
    overflow: hidden;
    border-bottom: 5px solid var(--orange);
    box-shadow: 0 10px 30px rgba(0,0,0,.45);
  }
  .card--front { left: 40px; background: var(--peach); }
  .card--back  { left: 630px; background: var(--paper); }

  .card__watermark {
    position: absolute;
    border-radius: 50%;
    background: radial-gradient(circle, var(--peach-deep) 0%, rgba(251,227,209,0) 70%);
  }
  .card--front .card__watermark { width: 420px; height: 420px; left: 120px; top: -80px; }
  .card--back .card__watermark  { width: 360px; height: 360px; right: -90px; top: 20px; }

  .brand {
    display: inline-flex;
    align-items: center;
    gap: 10px;
    border: 3px solid var(--orange);
    padding: 10px 18px;
  }
  .brand__mark { width: 18px; height: 18px; background: var(--orange); }
  .brand__name {
    font-weight: 800;
    color: var(--orange);
    letter-spacing: 2px;
    white-space: nowrap;
  }

  .card--front .brand {
    position: absolute;
    left: 50%; top: 78px;
    transform: translateX(-50%);
  }
  .card--front .brand__name { font-size: 36px; }

  .services {
    position: absolute;
    left: 0; right: 0; top: 200px;
    text-align: center;
    font-size: 14px;
    color: var(--ink);
    line-height: 1.7;
  }
  .services__item { display: inline-flex; align-items: center; gap: 5px; margin: 0 4px; }
  .services__bullet { width: 8px; height: 8px; background: var(--orange); display: inline-block; }

  .card--back .brand {
    position: absolute;
    left: 28px; top: 42px;
    padding: 7px 13px;
  }
  .card--back .brand__name { font-size: 24px; }
  .card--back .brand__mark { width: 13px; height: 13px; }

  .person {
    position: absolute;
    right: 30px; top: 40px;
    text-align: right;
  }
  .person__name { font-size: 24px; font-weight: 700; color: var(--orange); }
  .person__name span { color: var(--grey); }
  .person__title { font-size: 13px; font-weight: 600; color: var(--ink); letter-spacing: 1px; }
  .person__bar {
    position: absolute;
    right: 0; top: 40px;
    width: 14px; height: 48px;
    background: var(--orange);
  }

  .contact {
    position: absolute;
    left: 30px; bottom: 28px;
    list-style: none;
    font-size: 17px;
    color: var(--ink);
  }
  .contact__row { display: flex; align-items: center; gap: 10px; line-height: 1.55; }
  .contact__icon { width: 14px; height: 14px; fill: var(--orange); flex: none; }
</style>
</head>
<body>

<section class="card card--front">
  <div class="card__watermark" role="img" aria-label="Faint brand mark decoration"></div>
  <div class="brand">
    <span class="brand__mark"></span>
    <span class="brand__name">PELIKAR HIRES</span>
  </div>
  <div class="services">
    <div><span class="services__item"><i class="services__bullet"></i>Luxury Restroom Trailers Rental and Sales</span></div>
    <div>
      <span class="services__item"><i class="services__bullet"></i>Weddings</span>
      <span class="services__item"><i class="services__bullet"></i>Concerts</span>
      <span class="services__item"><i class="services__bullet"></i>Charity</span>
      <span class="services__item"><i class="services__bullet"></i>Sporting and Corp</span>
      <span class="services__item"><i class="services__bullet"></i>Events</span>
    </div>
  </div>
</section>

<section class="card card--back">
  <div class="card__watermark" role="img" aria-label="Faint brand mark decoration"></div>
  <div class="brand">
    <span class="brand__mark"></span>
    <span class="brand__name">PELIKAR HIRES</span>
  </div>
  <div class="person__bar"></div>
  <div class="person">
    <div class="person__name">Dennis <span>Moyle</span></div>
    <div class="person__title">CFO</div>
  </div>
  <ul class="contact">
    <li class="contact__row">
      <svg class="contact__icon" viewBox="0 0 24 24"><path d="M6.6 10.8a15.1 15.1 0 0 0 6.6 6.6l2.2-2.2a1 1 0 0 1 1-.25 11.4 11.4 0 0 0 3.6.57 1 1 0 0 1 1 1V20a1 1 0 0 1-1 1A17 17 0 0 1 3 4a1 1 0 0 1 1-1h3.5a1 1 0 0 1 1 1c0 1.25.2 2.45.57 3.57a1 1 0 0 1-.25 1z"/></svg>
      555 018-3647
    </li>
    <li class="contact__row">
      <svg class="contact__icon" viewBox="0 0 24 24"><path d="M2 5h20v14H2z M2 5l10 8 10-8" fill="none" stroke="#f26a21" stroke-width="2.5"/></svg>
      info@pelikarhires.com
    </li>
    <li class="contact__row">
      <svg class="contact__icon" viewBox="0 0 24 24"><circle cx="12" cy="12" r="10" fill="none" stroke="#f26a21" stroke-width="2.5"/><path d="M2 12h20M12 2c3 3 3 17 0 20M12 2c-3 3-3 17 0 20" fill="none" stroke="#f26a21" stroke-width="2"/></svg>
      www.pelikarhires.com
    </li>
  </ul>
</section>

</body>
</html>
```